Contractor Business Card Design

Looking to have a card made that has a bold description of (KITCHENS, BASEMENTS, BATHROOMS)

Definition and layers a plus

Contact info is;

Mark T. Ellery
Maplecrest, MN 55012
Cell: 612-555-0147
website: www.cobaltfinishworks.example
Email: cobaltfinishworksmn@mailbox.example

colors: red, black, gray, white

Contact Information for Business Card

Contact info is;

Mark T. Ellery
Maplecrest, MN 55012
Cell: 612-555-0147

Colors
ec1f27

Requirements
Must have
• Looking for layers and definition
Nice to have
• Cards are planned to be printed on plastic cards

```html
<!DOCTYPE html>
<html lang="en">
<head>
<meta charset="utf-8">
<title>Cobalt Finishworks – Business Card Design</title>
<link rel="stylesheet" href="https://fonts.googleapis.com/css2?family=Poppins:wght@400;500;700&family=Roboto:wght@400&display=swap">
<style>
  :root {
    --brand-red: #e80a0a;
    --brand-red-soft: #f25a5a;
    --ink: #111111;
    --text: #222222;
    --faint-gray: #dedede;
    --card-border: #8a8a8a;
    --white: #ffffff;
  }
  * { margin: 0; padding: 0; box-sizing: border-box; }
  html, body { width: 1200px; height: 927px; overflow: hidden; background: var(--white); }
  .sheet { position: relative; width: 1200px; height: 927px; }

  .sheet-title {
    position: absolute; top: 72px; left: 0; width: 100%;
    text-align: center; font-family: "Roboto", Arial, sans-serif; color: #000;
  }
  .sheet-title h1 { font-weight: 400; font-size: 38px; line-height: 44px; }
  .sheet-title p { font-size: 27px; line-height: 33px; }

  .card {
    position: absolute; top: 377px; width: 488px; height: 280px;
    border: 1px solid var(--card-border); background: var(--white); overflow: hidden;
    font-family: "Poppins", sans-serif;
  }
  .card-front { left: 67px; }
  .card-back { left: 645px; }

  .front-bar { position: absolute; left: 0; bottom: 0; width: 100%; height: 7px; background: var(--brand-red); }
  .front-decor { position: absolute; left: 312px; top: 26px; width: 230px; height: 230px; }

  .brand-mark {
    position: absolute; left: 115px; top: 72px; width: 88px; height: 88px;
    border: 4px solid var(--ink); border-radius: 50%; transform: translateX(-50%);
  }
  .brand-name {
    position: absolute; left: 15px; width: 200px; top: 174px;
    text-align: center; color: var(--ink); font-weight: 700;
    font-size: 18px; line-height: 23px; letter-spacing: 1px;
  }

  .holder-name {
    position: absolute; left: 226px; top: 64px;
    font-size: 18px; font-weight: 700; color: var(--ink);
  }
  .contact-list { position: absolute; left: 227px; top: 124px; list-style: none; }
  .contact-list li {
    display: flex; align-items: center; height: 25px;
    font-size: 11.4px; color: var(--text); white-space: nowrap;
  }
  .contact-list svg { width: 12px; height: 12px; margin-right: 9px; flex: none; fill: var(--brand-red); }

  .back-mark {
    position: absolute; left: 244px; top: 19px; width: 52px; height: 52px;
    border: 3px solid var(--ink); border-radius: 50%; transform: translateX(-50%);
  }
  .back-name {
    position: absolute; left: 0; width: 100%; top: 78px; text-align: center;
    font-weight: 700; font-size: 13px; letter-spacing: 1px; color: var(--ink);
  }

  .service-tile {
    position: absolute; top: 126px; width: 124px; height: 125px;
    background: var(--brand-red); border-radius: 6px; overflow: hidden;
  }
  .service-art {
    position: absolute; left: 12px; top: 8px; width: 100px; height: 84px;
    border-radius: 4px;
    background: linear-gradient(180deg, var(--brand-red-soft), var(--brand-red));
  }
  .service-tile span {
    position: absolute; left: 0; width: 100%; top: 98px; text-align: center;
    font-family: "Roboto", Arial, sans-serif; font-size: 17px; color: var(--white);
  }
  .tile-kitchens { left: 39px; }
  .tile-basements { left: 182px; }
  .tile-bathrooms { left: 324px; }
</style>
</head>
<body>
<main class="sheet">
  <header class="sheet-title">
    <h1>Cobalt Finishworks</h1>
    <p>Business Card Design</p>
    <p>Option -2</p>
  </header>

  <section class="card card-front">
    <svg class="front-decor" viewBox="0 0 230 230" aria-hidden="true">
      <circle cx="115" cy="115" r="105" fill="none" stroke="var(--faint-gray)" stroke-width="9"/>
    </svg>
    <div class="brand-mark" aria-hidden="true"></div>
    <div class="brand-name">COBALT<br>FINISHWORKS</div>

    <h2 class="holder-name">Mark T. Ellery</h2>
    <ul class="contact-list">
      <li><svg viewBox="0 0 12 12"><path d="M6 0a4.3 4.3 0 0 0-4.3 4.3C1.7 7.5 6 12 6 12s4.3-4.5 4.3-7.7A4.3 4.3 0 0 0 6 0zm0 6a1.7 1.7 0 1 1 0-3.4A1.7 1.7 0 0 1 6 6z"/></svg>Maplecrest, MN 55012</li>
      <li><svg viewBox="0 0 12 12"><path d="M3 0h6a1 1 0 0 1 1 1v10a1 1 0 0 1-1 1H3a1 1 0 0 1-1-1V1a1 1 0 0 1 1-1zm.6 1.4v9.2h4.8V1.4z"/></svg>612-555-0147</li>
      <li><svg viewBox="0 0 12 12"><path d="M0 2h12v1.2L6 7 0 3.2zM0 4.6l6 3.8 6-3.8V10H0z"/></svg>cobaltfinishworksmn@mailbox.example</li>
      <li><svg viewBox="0 0 12 12"><path fill="none" stroke="var(--brand-red)" stroke-width="1" d="M6 .6a5.4 5.4 0 1 0 0 10.8A5.4 5.4 0 0 0 6 .6zM.6 6h10.8M6 .6c-2.4 2.8-2.4 8 0 10.8M6 .6c2.4 2.8 2.4 8 0 10.8M1.4 3.4h9.2M1.4 8.6h9.2"/></svg>www.cobaltfinishworks.example</li>
    </ul>
    <div class="front-bar"></div>
  </section>

  <section class="card card-back">
    <div class="back-mark" aria-hidden="true"></div>
    <div class="back-name">COBALT FINISHWORKS</div>

    <div class="service-tile tile-kitchens">
      <div class="service-art" role="img" aria-label="White kitchen range hood illustration"></div>
      <span>KITCHENS</span>
    </div>

    <div class="service-tile tile-basements">
      <div class="service-art" role="img" aria-label="White house outline with basement stairs illustration"></div>
      <span>BASEMENTS</span>
    </div>

    <div class="service-tile tile-bathrooms">
      <div class="service-art" role="img" aria-label="White bathtub with shower head illustration"></div>
      <span>BATHROOMS</span>
    </div>
  </section>
</main>
</body>
</html>
```